Business Cards and Stationery for Background Check Company
Bluepine Tenant Vetting
Business Cards and Stationery for Background Check Company - Corporate Services
Creative Brief
Use same font as used in my logo
if you choose a different font from logo, please make sure it blends well
Professional
RK Delacroix
President
2745 S. Harrow Mill Ste 300 Southlake, TX 76094
888-417-6093 ext 342
rk@bluepinevet.com
www.bluepinevet.com
front side of the card - please use the white, black, gray, with red check
on the back side, please make the entire back of the card black and use the reverse logo
Concepts
Business Cards and Stationery for new compliance company.

```html
<!DOCTYPE html>
<html lang="en">
<head>
<meta charset="utf-8">
<title>Bluepine Tenant Vetting – Business Card</title>
<link rel="stylesheet" href="https://fonts.googleapis.com/css2?family=Open+Sans:wght@400;600;700&display=swap">
<style>
  :root {
    --page-bg: #e9e9e9;
    --card-white: #ffffff;
    --card-dark: #1f1f1f;
    --card-dark-edge: #2c2c2c;
    --accent-red: #d7262b;
    --soft-gray: #c9c9c9;
    --text-light: #f2f2f2;
    --text-muted: #b9b9b9;
    --logo-ink: #3a3a3a;
    --tagline: #8a8a8a;
  }
  * { box-sizing: border-box; margin: 0; padding: 0; }
  html, body {
    width: 1200px;
    height: 794px;
    overflow: hidden;
    background: var(--page-bg);
    font-family: "Open Sans", Arial, sans-serif;
  }
  .card {
    position: absolute;
    left: 150px;
    top: 140px;
    width: 900px;
    height: 514px;
    background: var(--card-white);
    box-shadow: 0 12px 30px rgba(0,0,0,0.18);
    overflow: hidden;
  }
  .card-shapes { position: absolute; inset: 0; }
  .brand {
    position: absolute;
    left: 150px;
    top: 262px;
    display: flex;
    flex-direction: column;
  }
  .brand-row { display: flex; align-items: center; gap: 10px; }
  .brand-name {
    font-weight: 700;
    font-size: 40px;
    letter-spacing: 1px;
    color: var(--logo-ink);
    line-height: 1;
  }
  .brand-square {
    width: 22px;
    height: 22px;
    background: var(--accent-red);
  }
  .brand-tagline {
    margin-top: 6px;
    font-size: 11px;
    letter-spacing: 3px;
    color: var(--tagline);
    text-transform: uppercase;
  }
  .person {
    position: absolute;
    right: 44px;
    top: 44px;
    text-align: right;
  }
  .person-name {
    font-weight: 700;
    font-size: 22px;
    color: var(--text-light);
  }
  .person-title {
    font-size: 17px;
    color: var(--text-muted);
    margin-top: 2px;
  }
  .contact {
    position: absolute;
    right: 44px;
    top: 210px;
    text-align: right;
    list-style: none;
    font-size: 15px;
    line-height: 25px;
    color: var(--text-light);
  }
  .contact li { display: flex; justify-content: flex-end; align-items: center; gap: 8px; }
  .contact .gap-above { margin-top: 14px; }
  .contact svg { width: 13px; height: 13px; fill: var(--text-light); }
</style>
</head>
<body>
  <div class="card">
    <svg class="card-shapes" viewBox="0 0 900 514" width="900" height="514" aria-hidden="true">
      <path d="M470 0 C 570 110, 590 360, 452 514" fill="none" stroke="var(--soft-gray)" stroke-width="4"/>
      <path d="M505 0 C 615 120, 620 380, 480 514 L900 514 L900 0 Z" fill="var(--card-dark)"/>
      <path d="M530 0 C 635 125, 640 380, 505 514" fill="none" stroke="var(--card-dark-edge)" stroke-width="6"/>
      <path d="M585 210 C 610 320, 575 440, 482 514 L512 514 C 600 440, 622 320, 585 210 Z" fill="var(--accent-red)"/>
    </svg>

    <div class="brand">
      <div class="brand-row">
        <span class="brand-name">BLUEPINE</span>
        <span class="brand-square"></span>
      </div>
      <span class="brand-tagline">Tenant vetting services</span>
    </div>

    <div class="person">
      <p class="person-name">Dana Whitlow-Reyes</p>
      <p class="person-title">Consultant</p>
    </div>

    <ul class="contact">
      <li>417 12th floor Plaza</li>
      <li>Harrow Mill Road SLK</li>
      <li>014 628 3905
        <svg viewBox="0 0 24 24"><path d="M6.6 10.8a15 15 0 0 0 6.6 6.6l2.2-2.2a1 1 0 0 1 1-.25 11.4 11.4 0 0 0 3.6.57 1 1 0 0 1 1 1V20a1 1 0 0 1-1 1A17 17 0 0 1 3 4a1 1 0 0 1 1-1h3.5a1 1 0 0 1 1 1c0 1.25.2 2.45.57 3.57a1 1 0 0 1-.25 1z"/></svg>
      </li>
      <li>014 628 3906
        <svg viewBox="0 0 24 24"><rect x="3" y="8" width="18" height="10" rx="1"/><rect x="7" y="3" width="10" height="6"/><rect x="7" y="15" width="10" height="6" fill="var(--card-dark)"/></svg>
      </li>
      <li class="gap-above">dana@bluepinevet.com
        <svg viewBox="0 0 24 24"><rect x="2" y="5" width="20" height="14" rx="1"/></svg>
      </li>
      <li>www.bluepinevet.com</li>
    </ul>
  </div>
</body>
</html>
```